Harbin Cargo needs a business card design.

Design a double-sided business card for new freight business. On the front, would like to see our logo along with the following info:

Nathaniel Voskuhl
CEO/FOUNDER
617-552-0194
nathanielvoskuhl@harbin-cargo.example

On the reverse side, we would like to use the graphic image of our logo only without the Harbin Cargo name.

```html
<!DOCTYPE html>
<html lang="en">
<head>
<meta charset="utf-8">
<title>Harbin Cargo — Business Card</title>
<link rel="stylesheet" href="https://fonts.googleapis.com/css2?family=Open+Sans:wght@400;600;700;800&display=swap">
<style>
  :root {
    --navy: #27225e;
    --navy-deep: #1d1a4d;
    --navy-light: #6f67b0;
    --red: #b8232b;
    --red-deep: #6e0f14;
    --white: #ffffff;
    --paper: #f2f2f3;
    --stage: #d9dadc;
    --ink: #27225e;
  }
  * { box-sizing: border-box; margin: 0; padding: 0; }
  html, body { width: 1200px; height: 900px; overflow: hidden; }
  body {
    background: var(--stage);
    font-family: "Open Sans", Arial, sans-serif;
    position: relative;
  }
  .card {
    position: absolute;
    left: 290px;
    width: 620px;
    height: 354px;
    box-shadow: 0 6px 18px rgba(0,0,0,0.25);
    overflow: hidden;
  }

  /* Reverse side */
  .card--back {
    top: 60px;
    background: linear-gradient(150deg, #2c2766 0%, var(--navy) 55%, var(--navy-deep) 100%);
  }
  .back-graphic {
    position: absolute;
    right: 0;
    top: 0;
    width: 330px;
    height: 260px;
    background: linear-gradient(135deg, var(--navy-light) 0%, var(--red) 55%, var(--red-deep) 100%);
    opacity: 0.9;
    border-bottom-left-radius: 40px;
  }

  /* Front side */
  .card--front {
    top: 480px;
    background: linear-gradient(100deg, var(--white) 0%, var(--paper) 100%);
  }
  .brand {
    position: absolute;
    left: 60px;
    top: 42px;
    display: flex;
    align-items: center;
    gap: 14px;
  }
  .brand-mark {
    width: 40px;
    height: 40px;
    background: var(--navy);
  }
  .brand-name {
    font-size: 36px;
    font-weight: 800;
    color: var(--navy);
    letter-spacing: 1px;
    line-height: 1;
  }
  .band {
    position: absolute;
    left: 0;
    top: 134px;
    width: 100%;
    height: 66px;
    background: linear-gradient(90deg, #3a3478 0%, var(--navy) 55%, var(--navy-deep) 100%);
  }
  .person {
    position: absolute;
    right: 40px;
    top: 8px;
    text-align: right;
  }
  .person-name {
    font-size: 23px;
    font-weight: 800;
    color: var(--red);
    line-height: 1.15;
    white-space: nowrap;
  }
  .person-title {
    font-size: 15px;
    font-weight: 400;
    color: var(--white);
    letter-spacing: 0.8px;
    line-height: 1.3;
  }
  .contacts {
    position: absolute;
    left: 40px;
    top: 226px;
    list-style: none;
  }
  .contact {
    display: flex;
    align-items: center;
    gap: 10px;
    font-size: 17px;
    color: var(--ink);
    line-height: 1.55;
    white-space: nowrap;
  }
  .contact svg { width: 15px; height: 15px; flex: none; }
  .contact svg * { stroke: var(--red); fill: none; stroke-width: 1.6; }
  .contact svg .solid { fill: var(--red); stroke: none; }
</style>
</head>
<body>

  <section class="card card--back" aria-label="Card reverse">
    <div class="back-graphic" role="img" aria-label="Company logo graphic"></div>
  </section>

  <section class="card card--front" aria-label="Card front">
    <div class="brand">
      <span class="brand-mark"></span>
      <span class="brand-name">Harbin Cargo</span>
    </div>

    <div class="band">
      <div class="person">
        <p class="person-name">Nathaniel Voskuhl</p>
        <p class="person-title">CEO/FOUNDER</p>
      </div>
    </div>

    <ul class="contacts">
      <li class="contact">
        <svg viewBox="0 0 16 16" aria-hidden="true"><path class="solid" d="M3 1.5l3 2.5-1.5 2.2a9 9 0 0 0 5.3 5.3L12 10l2.5 3-1.8 1.8C7 15 1 9 1.2 3.3z"/></svg>
        617-552-0194
      </li>
      <li class="contact">
        <svg viewBox="0 0 16 16" aria-hidden="true"><rect x="1.5" y="3.5" width="13" height="9"/><path d="M1.5 3.5l6.5 5 6.5-5"/></svg>
        nathanielvoskuhl@harbin-cargo.example
      </li>
      <li class="contact">
        <svg viewBox="0 0 16 16" aria-hidden="true"><circle cx="8" cy="8" r="6.5"/><path d="M1.5 8h13M8 1.5c-3 3.5-3 9.5 0 13M8 1.5c3 3.5 3 9.5 0 13"/></svg>
        www.harbin-cargo.example
      </li>
    </ul>
  </section>

</body>
</html>
```